The Illustrated Barnaby T. Wexcombe in China and Other Stories poster

I need a book promotional poster for my Author site and bookstores.

I have self-published a collection of historical adventures and need a striking poster that will engage young readers. I have attached a variety of images from the books and from a graphic-novel adaptation, so you should have plenty of visuals to work with.

Target Market(s)

Book readers

Industry/Entity Type

Publishing

Font styles to use
Serif
Other font styles liked:
• Caslon Antique is nice

Colors

Designer to choose colors to be used in the design.

Requirements
Must have
• I have attached a sample design sketch -- it is basically text background, a main image and spot illustrations along the bottom.
Nice to have
• I am open to your ideas as well --
Should not have
• A crowded look

```html
<!DOCTYPE html>
<html lang="en">
<head>
<meta charset="utf-8">
<title>The Illustrated Barnaby T. Wexcombe in China and Other Stories</title>
<link href="https://fonts.googleapis.com/css2?family=IM+Fell+English&family=Libre+Caslon+Text:ital,wght@0,400;0,700;1,400&display=swap" rel="stylesheet">
<style>
  :root {
    --page: #ffffff;
    --sky-grey: #8f7d73;
    --sky-rose: #e3a392;
    --sky-glow: #f1b38f;
    --sea-pink: #e6b2ac;
    --hull: #4a2c1c;
    --ink-dark: #3b2a22;
    --ink-light: #eef1f0;
    --ink-faint: rgba(240, 225, 218, 0.62);
    --frame: #ffffff;
  }
  * { margin: 0; padding: 0; box-sizing: border-box; }
  html, body { width: 1200px; height: 1200px; overflow: hidden; background: var(--page); }
  .poster {
    position: absolute; left: 54px; top: 190px; width: 1092px; height: 819px;
    overflow: hidden; font-family: "Libre Caslon Text", Georgia, serif;
  }
  .scene {
    position: absolute; inset: 0;
    background:
      radial-gradient(ellipse 60% 35% at 50% 58%, rgba(74, 44, 28, 0.75), rgba(74, 44, 28, 0) 70%),
      radial-gradient(ellipse 40% 30% at 85% 45%, rgba(246, 170, 130, 0.7), rgba(246, 170, 130, 0) 70%),
      linear-gradient(180deg, var(--sky-grey) 0%, var(--sky-rose) 40%, #d9b5a8 70%, var(--sea-pink) 100%);
  }
  .title {
    position: absolute; left: 16px; top: 12px;
    font-family: "IM Fell English", Georgia, serif; color: var(--ink-light);
    font-size: 46px; line-height: 1; font-weight: 400; white-space: nowrap;
  }
  .subtitle {
    position: absolute; left: 537px; top: 62px;
    font-family: "IM Fell English", Georgia, serif; color: var(--ink-light);
    font-size: 38px; line-height: 1; white-space: nowrap;
  }
  .quote { position: absolute; font-size: 14px; line-height: 1.36; }
  .quote cite { display: block; font-style: normal; font-weight: 400; }
  .quote cite i { font-style: italic; }
  .quote--faint { font-size: 12.4px; line-height: 16.6px; color: var(--ink-faint); width: 310px; }
  .quote--dark { color: var(--ink-dark); font-weight: 700; }
  .quote--dark cite { color: var(--ink-dark); }
  .quote--light { color: var(--ink-light); font-weight: 700; }
  .quote--light cite { color: var(--ink-light); }
  .q-premise { left: 50px; top: 148px; }
  .q-vital { left: 741px; top: 126px; width: 300px; }
  .q-fun { left: 842px; top: 262px; width: 240px; }
  .q-real { left: 31px; top: 350px; }
  .q-gorgeous { left: 790px; top: 404px; width: 290px; }
  .q-makings { left: 34px; top: 457px; width: 240px; }
  .q-cements { left: 703px; top: 553px; width: 380px; }
  .q-polished { left: 31px; top: 572px; width: 360px; }
  .spots { position: absolute; top: 638px; left: 350px; display: flex; gap: 25px; }
  .spot { width: 161px; height: 160px; border: 3px solid var(--frame); }
  .spot--night { background: linear-gradient(135deg, #3c2a6e, #6b3a7a 55%, #2b2350); }
  .spot--sail { background: linear-gradient(135deg, #c7c2c8, #e8e2d6 50%, #b4a7b8); }
  .spot--sketch { background: linear-gradient(135deg, #fbf3ee, #efd2c3); }
  .spot--ride { background: linear-gradient(135deg, #5b5f8a, #8a6a55 55%, #3a2c24); }
  .imprint { position: absolute; left: 14px; top: 714px; display: flex; align-items: flex-end; }
  .imprint-mark { width: 84px; height: 84px; border-radius: 50%; background: #f2ede8; border: 3px solid #3b3330; }
  .imprint-name { margin-left: 4px; margin-bottom: 4px; font-size: 20px; color: #2a2020; white-space: nowrap; }
</style>
</head>
<body>
<main class="poster">
  <div class="scene" role="img" aria-label="Painted sunset sky over a rolling sea with two sailing ships in battle, one on fire"></div>

  <h1 class="title">The Illustrated Barnaby T. Wexcombe</h1>
  <p class="subtitle">and other stories</p>

  <blockquote class="quote quote--faint q-premise">
    It’s a clever premise, to have teenaged heroes coming of age as well as changing the course of history, aided by the mysterious Navigators. This is a surefire series. I would recommend this to anyone who likes Owen Marsh, Harold Venn, Clara Dovesky or Desmond Achard.
    <cite>Nora Pell, <i>Lantern Lane Books</i></cite>
  </blockquote>

  <blockquote class="quote quote--faint q-vital">
    At a time when history seems particularly vital and textbooks seem increasingly bland, a series of historical novels like this is refreshing, and muchneeded. Substantive and entertaining …
    <cite>Maren J. Holt, <i>Lantern Lane Books</i></cite>
  </blockquote>

  <blockquote class="quote quote--dark q-fun">
    So. Much. Fun! I never wanted to stop reading …
    <cite>Open Shelf Reviews</cite>
  </blockquote>

  <blockquote class="quote quote--light q-real">
    Tom Harwell is the real thing.
    <cite>Cal Brenner, <i>Orders of Battle</i></cite>
  </blockquote>

  <blockquote class="quote quote--light q-gorgeous">
    Gorgeously written … the characters are clever, selfdriven, and unique.
    <cite>Jolene Fairs, <i>CozyPage Book Blog</i></cite>
  </blockquote>

  <blockquote class="quote quote--dark q-makings">
    This has all the makings of a wonderful literary property …
    <cite>Tessa Moore, Birch Row Books</cite>
  </blockquote>

  <blockquote class="quote quote--dark q-cements">
    Harwell cements himself as a brilliant storyteller of history … a wonderful, wonderful read.
    <cite><i>Tales at Dusk</i> book blog</cite>
  </blockquote>

  <blockquote class="quote quote--light q-polished" style="font-weight:400">
    “The Sultan’s Ledger” is an exceedingly polished and well-crafted story. Meticulously researched … complex and interesting.
    <cite>Elise Ward Conley</cite>
  </blockquote>

  <div class="spots">
    <div class="spot spot--night" role="img" aria-label="Moody violet painting of a figure at night"></div>
    <div class="spot spot--sail" role="img" aria-label="Painting of a young woman in front of a ship's sail"></div>
    <div class="spot spot--sketch" role="img" aria-label="Graphic-novel storyboard sketch page in sepia ink"></div>
    <div class="spot spot--ride" role="img" aria-label="Painting of riders on horseback in a skirmish"></div>
  </div>

  <div class="imprint">
    <span class="imprint-mark"></span>
    <span class="imprint-name">Meridian Harbor Press</span>
  </div>
</main>
</body>
</html>
```